Vexora and pinlark ads

Create four total ads, two for vexora and two for pinlark for classfinchly.com.

The pinlark ads will be a single image, and I will handle the text. Image should be consistent with this: https://notes.plankweave.net/image-ad-specs. Image ratio is 1200x628 with an Image ratio of 1.91:1.

Target Market(s)

Parents who have young kids and are thinking about moving to a better school district.

Industry/Entity Type

Real Estate

Font styles to use
Sans Serif

Requirements
Must have
• Classfinchly logo.

```html
<!DOCTYPE html>
<html lang="en">
<head>
<meta charset="utf-8">
<title>Classfinchly display ads</title>
<link href="https://fonts.googleapis.com/css2?family=Montserrat:wght@300;400;500;700&display=swap" rel="stylesheet">
<style>
  :root {
    --page-top: #fbfbfb;
    --page-bottom: #efefef;
    --sky: #26a7e2;
    --sky-light: #3fc0f4;
    --sky-deep: #1f98d4;
    --label: #2aa8e0;
    --white: #ffffff;
    --navy: #16184a;
    --go-dark: #1d6f98;
    --url: #2aa3dc;
  }
  * { box-sizing: border-box; margin: 0; padding: 0; }
  html, body { width: 1200px; height: 1200px; overflow: hidden; }
  body {
    position: relative;
    font-family: "Montserrat", sans-serif;
    background: linear-gradient(180deg, var(--page-top) 0%, var(--page-bottom) 100%);
  }
  .size-label {
    position: absolute;
    font-weight: 400;
    font-size: 23px;
    color: var(--label);
    transform: translateX(-50%);
    white-space: nowrap;
  }
  .size-label--small { font-size: 19px; }
  .ad {
    position: absolute;
    overflow: hidden;
    color: var(--white);
    background: linear-gradient(200deg, var(--sky-light) 0%, var(--sky) 45%, var(--sky-deep) 100%);
    box-shadow: 0 4px 14px rgba(0,0,0,0.12);
  }
  .ad--skyscraper { left: 295px; top: 255px; width: 240px; height: 480px; }
  .ad--rectangle { left: 618px; top: 385px; width: 240px; height: 200px; }
  .ad--leaderboard { left: 295px; top: 789px; width: 582px; height: 72px; }

  .brand-mark {
    position: absolute;
    border-radius: 50%;
    border: 3px solid rgba(255,255,255,0.9);
  }
  .headline {
    position: absolute;
    left: 0; right: 0;
    text-align: center;
    font-weight: 300;
    white-space: nowrap;
  }
  .headline b { font-weight: 700; }

  .go-link {
    position: absolute;
    display: flex;
    background: var(--white);
    border-radius: 3px;
    overflow: hidden;
    box-shadow: 0 2px 4px rgba(0,0,0,0.15);
  }
  .go-link__badge {
    background: var(--go-dark);
    color: var(--white);
    font-weight: 700;
    display: flex;
    flex-direction: column;
    align-items: center;
    justify-content: center;
    line-height: 1;
  }
  .go-link__badge svg { display: block; }
  .go-link__url {
    color: var(--url);
    font-weight: 400;
    display: flex;
    align-items: center;
    white-space: nowrap;
  }

  .brand-tab { position: absolute; display: block; }
  .brand-name {
    position: absolute;
    display: flex;
    align-items: center;
    gap: 6px;
    color: var(--navy);
    font-weight: 700;
    white-space: nowrap;
    transform: translate(-50%, -50%);
  }
  .brand-name__dot {
    border-radius: 50%;
    background: var(--sky);
    flex: none;
  }
</style>
</head>
<body>

  <div class="size-label" style="left:406px; top:210px;">300x600</div>
  <section class="ad ad--skyscraper">
    <div class="brand-mark" role="img" aria-label="Classfinchly brand mark" style="left:80px; top:32px; width:80px; height:80px;"></div>
    <div class="headline" style="top:133px; font-size:27px; line-height:31.5px;">
      Find the<br><b>Top 30</b><br><b>Chicagoland</b><br><b>Schools</b><br>with Homes<br>for Sale
    </div>
    <div class="go-link" style="left:26px; top:346px; width:184px; height:29px;">
      <div class="go-link__badge" style="width:25px; font-size:11px;">GO
        <svg width="16" height="5" viewBox="0 0 16 5"><path d="M0 2.5H14M11.5 0.5L14 2.5 11.5 4.5" stroke="#fff" stroke-width="1" fill="none"/></svg>
      </div>
      <div class="go-link__url" style="padding-left:4px; font-size:12.3px;">www.classfinchly.com</div>
    </div>
    <svg class="brand-tab" style="left:0; top:418px;" width="240" height="62" viewBox="0 0 240 62">
      <path d="M0 62 L20 10 Q24 0 36 0 L204 0 Q216 0 220 10 L240 62 Z" fill="#fff"/>
    </svg>
    <div class="brand-name" style="left:120px; top:449px; font-size:19px;">
      <span class="brand-name__dot" style="width:14px; height:14px;"></span>Classfinchly
    </div>
  </section>

  <section class="ad ad--rectangle">
    <div class="brand-mark" role="img" aria-label="Classfinchly brand mark" style="left:96px; top:8px; width:48px; height:48px; border-width:2px;"></div>
    <div class="headline" style="top:64px; font-size:18px; line-height:19px;">
      Find the <b>Top 30</b><br><b>Chicagoland Schools</b><br>with Homes for Sale
    </div>
    <div class="go-link" style="left:34px; top:130px; width:174px; height:18px;">
      <div class="go-link__badge" style="width:18px; font-size:8px;">GO
        <svg width="11" height="4" viewBox="0 0 11 4"><path d="M0 2H10M8 0.5L10 2 8 3.5" stroke="#fff" stroke-width="0.8" fill="none"/></svg>
      </div>
      <div class="go-link__url" style="padding-left:6px; font-size:10.5px; letter-spacing:0.3px;">www.classfinchly.com</div>
    </div>
    <svg class="brand-tab" style="left:0; top:162px;" width="240" height="38" viewBox="0 0 240 38">
      <path d="M0 38 L22 7 Q27 0 36 0 L204 0 Q213 0 218 7 L240 38 Z" fill="#fff"/>
    </svg>
    <div class="brand-name" style="left:120px; top:184px; font-size:16px;">
      <span class="brand-name__dot" style="width:11px; height:11px;"></span>Classfinchly
    </div>
  </section>
  <div class="size-label" style="left:737px; top:611px;">300x250</div>

  <section class="ad ad--leaderboard">
    <div class="brand-mark" role="img" aria-label="Classfinchly brand mark" style="left:22px; top:8px; width:56px; height:56px; border-width:2px;"></div>
    <div class="headline" style="left:0; right:auto; width:546px; top:6px; font-size:17.5px; line-height:18.5px;">
      Find the <b>Top 30 Chicagoland Schools</b><br>with Homes for Sale
    </div>
    <div class="go-link" style="left:175px; top:46px; width:192px; height:17px;">
      <div class="go-link__badge" style="width:18px; font-size:8px;">GO
        <svg width="11" height="4" viewBox="0 0 11 4"><path d="M0 2H10M8 0.5L10 2 8 3.5" stroke="#fff" stroke-width="0.8" fill="none"/></svg>
      </div>
      <div class="go-link__url" style="padding-left:7px; font-size:11px; letter-spacing:0.6px;">www.classfinchly.com</div>
    </div>
    <svg class="brand-tab" style="left:386px; top:33px;" width="196" height="39" viewBox="0 0 196 39">
      <path d="M0 39 L24 7 Q29 0 38 0 L196 0 L196 39 Z" fill="#fff"/>
    </svg>
    <div class="brand-name" style="left:494px; top:54px; font-size:16px;">
      <span class="brand-name__dot" style="width:11px; height:11px;"></span>Classfinchly
    </div>
  </section>
  <div class="size-label size-label--small" style="left:586px; top:874px;">728x90</div>

</body>
</html>
```